Etiketten für Honig
Zielgruppe
Imkerei Kolbach / Verkauf von Honig - eigene Völker ( Produktion)
Zielgruppe: Privatpersonen (Freunde, Bekannte) keine Zwischenhändler
Aufgabenstellung
Ich wohne in einem alten Fachwerkhaus, welches ursprünglich als Schmiede gebaut wurde.
Honig& Schmiede oder Biene & Schmiede sollten berücksichtigt werden
Stichwort: Schmiedehonig oder so ähnlich
Etiketten mit Verbraucherschutz
Ursprung Deutschland
Gläser: Neutral
Abmessungen:
•Durchmesser: 8,05 cm
•Gesamthöhe: 9,4 cm
•Höhe ohne Gewinde: 8,05 cm

```html
<!DOCTYPE html>
<html lang="de">
<head>
<meta charset="utf-8">
<title>Waldhonig – Etikett</title>
<link rel="stylesheet" href="https://fonts.googleapis.com/css2?family=Montserrat:wght@400;600&family=Roboto+Condensed:wght@300;700&display=swap">
<style>
  :root {
    --canvas: #e9e9e9;
    --paper: #ffffff;
    --charcoal: #222222;
    --gold: #b38b36;
    --white: #ffffff;
    --honey-dark: #6b2a12;
    --honey: #c0501c;
    --honey-amber: #d98a2a;
    --honey-light: #f0b45a;
    --comb-violet: #7f6b9a;
    --fire-dark: #1a1410;
    --fire: #c9501e;
  }
  * { margin: 0; padding: 0; box-sizing: border-box; }
  html, body { width: 1200px; height: 1200px; overflow: hidden; }
  body {
    background: var(--canvas);
    position: relative;
    font-family: "Roboto Condensed", sans-serif;
  }

  /* Upper white field with diagonal edge */
  .upper-field {
    position: absolute;
    inset: 0;
    background: var(--paper);
    clip-path: polygon(0 0, 100% 0, 100% 635px, 0 748px);
  }
  .honey-photo {
    position: absolute;
    right: 0; top: 0;
    width: 440px; height: 680px;
    background:
      radial-gradient(ellipse 40% 30% at 75% 12%, var(--honey-light) 0%, rgba(240,180,90,0) 100%),
      linear-gradient(100deg, rgba(217,138,42,0) 0%, rgba(217,138,42,0) 45%, var(--honey-amber) 62%, var(--honey) 100%);
    clip-path: polygon(0 0, 100% 0, 100% 635px, 0 675px);
  }

  /* Brand tile */
  .brand-tile {
    position: absolute;
    left: 203px; top: 0;
    width: 203px; height: 203px;
    background: var(--charcoal);
    display: flex; flex-direction: column;
    align-items: center; justify-content: center;
    gap: 4px;
    padding-top: 20px;
  }
  .brand-name {
    font-family: "Montserrat", sans-serif;
    font-weight: 400;
    color: var(--gold);
    text-align: center;
    letter-spacing: 0.14em;
    line-height: 1.3;
  }
  .brand-tile .brand-name { font-size: 19px; }
  .brand-dot {
    width: 12px; height: 12px; border-radius: 50%;
    background: var(--gold);
    margin-bottom: 8px;
  }

  /* Label */
  .label {
    position: absolute;
    left: 343px; top: 815px;
    width: 543px; height: 262px;
    background: var(--charcoal);
    overflow: hidden;
  }
  .label-visual {
    position: relative;
    height: 151px;
    display: flex;
  }
  .photo-comb {
    width: 50%; height: 100%;
    background: linear-gradient(120deg, var(--honey-dark) 0%, var(--honey) 35%, var(--comb-violet) 65%, var(--honey) 100%);
  }
  .photo-forge {
    width: 50%; height: 100%;
    background: radial-gradient(ellipse at 45% 85%, #f0a040 0%, var(--fire) 25%, #4a1e10 55%, var(--fire-dark) 85%);
  }
  .product-name {
    position: absolute;
    left: 0; right: 0; top: 50px;
    text-align: center;
    font-family: "Montserrat", sans-serif;
    font-weight: 600;
    font-size: 44px;
    letter-spacing: -0.01em;
    color: var(--white);
  }
  .net-weight {
    position: absolute;
    right: 19px; top: 16px;
    font-family: "Montserrat", sans-serif;
    font-weight: 600;
    font-size: 12px;
    color: var(--gold);
  }
  .label-info {
    position: relative;
    height: 111px;
    color: var(--white);
    font-weight: 300;
    font-size: 11.5px;
    line-height: 12.8px;
  }
  .producer {
    position: absolute;
    left: 20px; top: 30px;
  }
  .producer .web { font-weight: 700; margin-top: 1px; }
  .label-info .brand {
    position: absolute;
    left: 50%; top: 18px;
    transform: translateX(-50%);
    display: flex; flex-direction: column; align-items: center;
  }
  .label-info .brand-name { font-size: 12.5px; }
  .label-info .brand-dot { width: 7px; height: 7px; margin-bottom: 10px; }
  .storage {
    position: absolute;
    right: 19px; top: 30px;
    text-align: right;
  }
  .storage .best-before { margin-top: 10px; font-size: 9.5px; }
</style>
</head>
<body>

  <div class="upper-field">
    <div class="honey-photo" role="img" aria-label="Foto: Honigstab, von dem goldener Honig herabfließt"></div>
  </div>

  <div class="brand-tile">
    <span class="brand-dot"></span>
    <div class="brand-name">IMKEREI<br>KOLBACH</div>
  </div>

  <div class="label">
    <div class="label-visual">
      <div class="photo-comb" role="img" aria-label="Foto: Nahaufnahme von Honigwaben in Bernstein- und Violetttönen"></div>
      <div class="photo-forge" role="img" aria-label="Foto: Schmiedefeuer mit Flammen und Funken im Dunkeln"></div>
      <div class="product-name">Waldhonig</div>
      <div class="net-weight">500g</div>
    </div>
    <div class="label-info">
      <div class="producer">
        Imkerei Kolbach<br>
        Musterstraße 1<br>
        12345 Musterstadt<br>
        Tel: 0123 /456
        <div class="web">www.imkerei-kolbach.de</div>
      </div>
      <div class="brand">
        <span class="brand-dot"></span>
        <div class="brand-name">IMKEREI<br>KOLBACH</div>
      </div>
      <div class="storage">
        Trocken und vor Wärme<br>geschützt lagern!
        <div class="best-before">Mindesten haltbar bis:</div>
      </div>
    </div>
  </div>

</body>
</html>
```